Brightstone Roofing Business Card

This is my current business card. But I’d like to make some changes. Somewhere on the card I’d like to list some of the services we offer. Maybe on the back? But I’d still like to keep the red. White and black modern look.

-residential & commercial roofing
-Roof Repairs & Maintenance
-Storm Damage & Insurance Claims specialist
-Christmas Lights and permanent Christmas lights
Fencing. Windows. Gutters. Siding. Sheetrock, painting.

```html
<!DOCTYPE html>
<html lang="en">
<head>
<meta charset="utf-8">
<title>Brightstone Roofing Business Card</title>
<link href="https://fonts.googleapis.com/css2?family=Michroma&family=Montserrat:wght@600;800&family=Nunito+Sans:wght@400&family=Roboto:wght@400&display=swap" rel="stylesheet">
<style>
  :root {
    --page: #ffffff;
    --card: #000000;
    --chevron: #1b1b1b;
    --rule: #2e2e2e;
    --red: #e3161b;
    --white: #ffffff;
  }
  * { margin: 0; padding: 0; box-sizing: border-box; }
  html, body { width: 1200px; height: 1000px; overflow: hidden; background: var(--page); }
  .card {
    position: absolute;
    width: 610px;
    height: 349px;
    background: var(--card);
    overflow: hidden;
    color: var(--white);
  }
  .card--front { left: 286px; top: 137px; }
  .card--back { left: 289px; top: 526px; }
  .chevrons { position: absolute; left: 0; top: 0; width: 610px; height: 349px; }
  .chevrons polygon { fill: var(--chevron); }

  .brand {
    position: absolute;
    left: 0; right: 0;
    top: 90px;
    display: flex;
    flex-direction: column;
    align-items: center;
  }
  .brand__dot {
    width: 102px; height: 102px;
    border-radius: 50%;
    background: var(--red);
    border: 3px solid var(--white);
  }
  .brand__name {
    margin-top: 14px;
    font-family: "Montserrat", sans-serif;
    font-weight: 800;
    font-size: 22px;
    letter-spacing: 1px;
    line-height: 1.15;
    text-align: center;
    color: var(--white);
  }

  .person { position: absolute; left: 45px; top: 38px; }
  .person__name {
    font-family: "Michroma", sans-serif;
    font-size: 20px;
    letter-spacing: 1px;
    line-height: 1;
  }
  .person__first { color: var(--red); }
  .person__role {
    margin-top: 9px;
    font-family: "Nunito Sans", sans-serif;
    font-size: 14.5px;
  }
  .person__role span { color: var(--red); }
  .rule { position: absolute; height: 3px; background: var(--rule); }
  .rule--top { left: 0; top: 97px; width: 248px; }
  .rule--contact { left: 387px; top: 266px; width: 223px; }
  .rule--base { left: 100px; top: 337px; width: 510px; height: 12px; background: var(--chevron); }

  .services { position: absolute; left: 47px; top: 112px; list-style: none; }
  .services li {
    position: relative;
    padding-left: 14px;
    font-family: "Montserrat", sans-serif;
    font-weight: 600;
    font-size: 14.6px;
    line-height: 18px;
    margin-bottom: 12.5px;
  }
  .services li::before {
    content: "";
    position: absolute;
    left: 0; top: 2px; bottom: -4px;
    width: 5px;
    background: var(--red);
  }

  .contact {
    position: absolute;
    display: flex;
    align-items: center;
    gap: 6px;
    font-family: "Roboto", sans-serif;
  }
  .contact svg { fill: var(--white); flex: none; }
  .contact--phone { left: 387px; top: 274px; font-size: 23px; letter-spacing: 1.5px; }
  .contact--web { left: 387px; top: 309px; font-size: 14.5px; }
  .contact--mail { left: 43px; top: 309px; font-size: 14.5px; }
</style>
</head>
<body>

<section class="card card--front">
  <svg class="chevrons" viewBox="0 0 610 349" aria-hidden="true">
    <polygon points="328,-22 391,-22 528,110 665,-22 728,-22 528,172"/>
    <polygon points="419,-22 473,-22 528,30 583,-22 637,-22 528,84"/>
    <polygon points="-60,349 31,258 122,349 97,349 31,283 -35,349"/>
    <polygon points="-40,349 31,278 102,349 84,349 31,296 -22,349"/>
  </svg>
  <div class="brand">
    <div class="brand__dot"></div>
    <p class="brand__name">BRIGHTSTONE<br>ROOFING CO.</p>
  </div>
</section>

<section class="card card--back">
  <svg class="chevrons" viewBox="0 0 610 349" aria-hidden="true">
    <polygon points="328,-22 391,-22 528,110 665,-22 728,-22 528,172"/>
    <polygon points="419,-22 473,-22 528,30 583,-22 637,-22 528,84"/>
    <polygon points="-60,349 31,258 122,349 97,349 31,283 -35,349"/>
    <polygon points="-40,349 31,278 102,349 84,349 31,296 -22,349"/>
  </svg>

  <div class="person">
    <h1 class="person__name"><span class="person__first">DEAN</span> CARVER</h1>
    <p class="person__role">Roofing Contractor in <span>Texas</span></p>
  </div>
  <div class="rule rule--top"></div>

  <ul class="services">
    <li>Residential &amp; Commercial Roofing.</li>
    <li>Roof Repairs &amp; Maintenance.</li>
    <li>Storm Damage &amp; Insurance Claims Specialist.</li>
    <li>Christmas Lights and Permanent Christmas lights,<br>Fencing, Windows, Gutters, Siding, Sheetrock, Painting.</li>
  </ul>

  <div class="rule rule--contact"></div>
  <p class="contact contact--phone">
    <svg width="13" height="13" viewBox="0 0 24 24" aria-hidden="true"><path d="M6.6 10.8a15.1 15.1 0 0 0 6.6 6.6l2.2-2.2a1 1 0 0 1 1-.25 11.4 11.4 0 0 0 3.6.57 1 1 0 0 1 1 1V20a1 1 0 0 1-1 1A17 17 0 0 1 3 4a1 1 0 0 1 1-1h3.5a1 1 0 0 1 1 1c0 1.25.2 2.45.57 3.57a1 1 0 0 1-.25 1z"/></svg>
    555-014-2387
  </p>
  <p class="contact contact--web">
    <svg width="12" height="12" viewBox="0 0 24 24" aria-hidden="true"><path d="M12 2a10 10 0 1 0 0 20 10 10 0 0 0 0-20zm6.9 6h-3a15.6 15.6 0 0 0-1.4-3.6A8 8 0 0 1 18.9 8zM12 4a14 14 0 0 1 1.9 4h-3.8A14 14 0 0 1 12 4zM4.3 14a8 8 0 0 1 0-4h3.4a16 16 0 0 0 0 4zm.8 2h3a15.6 15.6 0 0 0 1.4 3.6A8 8 0 0 1 5.1 16zm3-8h-3a8 8 0 0 1 4.4-3.6A15.6 15.6 0 0 0 8.1 8zM12 20a14 14 0 0 1-1.9-4h3.8A14 14 0 0 1 12 20zm2.3-6H9.7a14.7 14.7 0 0 1 0-4h4.6a14.7 14.7 0 0 1 0 4zm.2 5.6a15.6 15.6 0 0 0 1.4-3.6h3a8 8 0 0 1-4.4 3.6zm1.8-5.6a16 16 0 0 0 0-4h3.4a8 8 0 0 1 0 4z"/></svg>
    www.brightstoneroofing.co
  </p>
  <p class="contact contact--mail">
    <svg width="16" height="12" viewBox="0 0 24 18" aria-hidden="true"><path d="M0 0h24v18H0zm2 2.4V16h20V2.4l-10 8zM3.5 2 12 8.8 20.5 2z"/></svg>
    dean@brightstoneroofing.co
  </p>
  <div class="rule rule--base"></div>
</section>

</body>
</html>
```